Hispanic Financial Counseling and Advocate Firm seeks business card design

Looking for a clean, professional business card design. This is a firm that specializes in providing financial education, coaching, and planning to the Hispanic community. The name of the company is Valemar, which means to prosper. We need a design that is clean, professional, and invokes trust, professionalism, but also welcoming. Our logo is a plant growing from a hand to give the messaging of of being in control of growing your financial future and security. Its part of a larger organization names Celesta Financial Group, who's logo is a tree with multi colored branches. We have the back of the card designed so we just need the front designed. the back is blue, so front needs to be a different background color, not blue.

Target Market(s)

Hispanic Community looking to better their future

Industry/Entity Type

financial services

Contact Information for Business Card

contact info: Anselmo Ibarra Jr, 951-555-0147, info@celestafinancialgroup.example. Celestafinancialgroup.example. tag line: Para un futuro mas seguro!

Requirements
Must have
• basics: logo, contact info.
Nice to have
• possibly incorporate the tree logo provided somehow
Should not have
• should not look like the back, needs to be different from the back provided.

```html
<!DOCTYPE html>
<html lang="es">
<head>
<meta charset="utf-8">
<title>Celesta Financial Group – Business Card</title>
<link href="https://fonts.googleapis.com/css2?family=Montserrat:wght@400;500;600;700&display=swap" rel="stylesheet">
<style>
  :root{
    --navy:#0f3447;
    --ink:#0f3447;
    --white:#ffffff;
    --page:#e6e8eb;
    --red:#ee4b55;
    --blue:#1fa3dc;
    --green:#8cc63f;
    --purple:#a98bc8;
    --yellow:#f7c41d;
    --valemar:#5aa43a;
    --muted:#4a5560;
  }
  *{box-sizing:border-box;margin:0;padding:0}
  html,body{width:1200px;height:913px;overflow:hidden}
  body{background:var(--page);font-family:'Montserrat',sans-serif;position:relative}

  .card{position:absolute;left:290px;width:620px;height:354px;border-radius:18px;overflow:hidden;box-shadow:0 6px 20px rgba(0,0,0,.18)}
  .card--back{top:56px;background:var(--navy);color:var(--white)}
  .card--front{top:476px;background:var(--white);color:var(--ink)}

  /* back */
  .brand-block{position:absolute;left:44px;top:118px;font-weight:600;line-height:1}
  .brand-block .brand-name{font-size:68px;letter-spacing:-2px}
  .brand-block .brand-sub{font-size:21px;margin-top:6px;letter-spacing:.5px}
  .hero-art{position:absolute;right:0;top:0;width:300px;height:270px;border-bottom-left-radius:140px;
    background:radial-gradient(circle at 40% 45%,var(--green) 0,var(--blue) 30%,var(--red) 55%,var(--purple) 75%,var(--navy) 100%);opacity:.9}
  .services{position:absolute;left:44px;top:262px;font-size:15px;font-weight:500;line-height:1.6;list-style:none}
  .services .row{display:block}
  .services .item{display:inline-flex;align-items:center;margin-right:14px}
  .dot{width:8px;height:8px;border-radius:50%;margin-right:7px;display:inline-block}

  /* front */
  .tree-mark{position:absolute;left:40px;top:150px;width:100px;height:100px;border-radius:50%;
    background:radial-gradient(circle at 50% 40%,var(--yellow) 0,var(--green) 25%,var(--blue) 50%,var(--red) 72%,var(--white) 100%)}
  .divider{position:absolute;left:158px;top:144px;width:1px;height:112px;background:var(--ink)}
  .front-brand{position:absolute;left:174px;top:164px;font-weight:600;line-height:1;color:var(--ink)}
  .front-brand .brand-name{font-size:44px;letter-spacing:-1.5px}
  .front-brand .brand-sub{font-size:13px;margin-top:4px}

  .person{position:absolute;left:318px;top:36px;width:280px}
  .person h1{font-size:20px;font-weight:700;letter-spacing:.3px;margin-bottom:10px;white-space:nowrap}
  .contact{list-style:none;font-size:12.5px;color:var(--muted);line-height:1.8}
  .contact li{display:flex;align-items:center;gap:8px;white-space:nowrap}
  .contact svg{width:13px;height:13px;flex:none}

  .partner{position:absolute;right:34px;top:196px;display:flex;align-items:center;gap:8px;font-size:22px;font-weight:600;color:var(--valemar)}
  .partner .mark{width:13px;height:13px;border-radius:50%;background:var(--valemar)}

  .tagline{position:absolute;left:300px;top:290px;font-size:16px;color:var(--muted);font-weight:500}

  .color-band{position:absolute;left:0;bottom:0;width:100%;height:9px;display:flex}
  .color-band span{flex:1}
</style>
</head>
<body>

<section class="card card--back" aria-label="Reverso de la tarjeta">
  <div class="hero-art" role="img" aria-label="Ilustración de una mano sosteniendo un árbol con hojas multicolores"></div>
  <div class="brand-block">
    <div class="brand-name">Celesta</div>
    <div class="brand-sub">Financial Group Inc</div>
  </div>
  <div class="services">
    <div class="row">
      <span class="item"><span class="dot" style="background:var(--green)"></span>Inmigración</span>
      <span class="item"><span class="dot" style="background:var(--purple)"></span>Planificacion Financiera</span>
    </div>
    <div class="row">
      <span class="item"><span class="dot" style="background:var(--yellow)"></span>Seguros</span>
      <span class="item"><span class="dot" style="background:var(--red)"></span>Impuestos</span>
      <span class="item"><span class="dot" style="background:var(--blue)"></span>Y mas</span>
    </div>
    <div class="row">
      <span class="item"><span class="dot" style="background:var(--green)"></span>Preparación de documentos</span>
    </div>
  </div>
</section>

<section class="card card--front" aria-label="Frente de la tarjeta">
  <div class="tree-mark" role="img" aria-label="Emblema de árbol con ramas multicolores"></div>
  <div class="divider"></div>
  <div class="front-brand">
    <div class="brand-name">Celesta</div>
    <div class="brand-sub">Financial Group Inc</div>
  </div>

  <div class="person">
    <h1>Anselmo Ibarra Jr</h1>
    <ul class="contact">
      <li>
        <svg viewBox="0 0 24 24"><path fill="var(--blue)" d="M6.6 10.8a15 15 0 0 0 6.6 6.6l2.2-2.2c.3-.3.7-.4 1-.2 1.1.4 2.3.6 3.6.6.6 0 1 .4 1 1V20c0 .6-.4 1-1 1A17 17 0 0 1 3 4c0-.6.4-1 1-1h3.5c.6 0 1 .4 1 1 0 1.3.2 2.5.6 3.6.1.3 0 .7-.2 1z"/></svg>
        951-555-0147
      </li>
      <li>
        <svg viewBox="0 0 24 24"><rect x="2" y="5" width="20" height="14" rx="2" fill="var(--red)"/><path d="M2 6l10 7 10-7" stroke="#fff" stroke-width="2" fill="none"/></svg>
        info@celestafinancialgroup.example
      </li>
      <li>
        <svg viewBox="0 0 24 24"><circle cx="12" cy="12" r="10" fill="var(--purple)"/><path d="M2 12h20M12 2c3 3 3 17 0 20M12 2c-3 3-3 17 0 20" stroke="#fff" stroke-width="1.5" fill="none"/></svg>
        Celestafinancialgroup.example
      </li>
    </ul>
  </div>

  <div class="partner"><span class="mark"></span>Valemar</div>

  <p class="tagline">Para un futuro mas seguro!</p>

  <div class="color-band">
    <span style="background:var(--red)"></span>
    <span style="background:var(--blue)"></span>
    <span style="background:var(--green)"></span>
    <span style="background:var(--purple)"></span>
    <span style="background:var(--yellow)"></span>
  </div>
</section>

</body>
</html>
```